Create modern and sleek business card for luxury real estate company

We're a "boutique" real estate office looking for a design that gets across a highly modern luxury brand. Blacks and whites are probably the best colors unless we try a silver foil for the logo. I've attached a version of our current logo here. I'd like to swap out the current font on there with Gotham Light Regular.

I'm looking to have one side of the card have the logo with the space for our agents info on the other side.

Target Market(s)

Young professionals in a "luxury" headspace

Industry/Entity Type

Real estate

Contact Information for Business Card

A place for agent name, cell number, website. The slogan "Quietly Redefining Fine Homes".

Font styles to use
Other font styles liked:
• Gotham Regular

Colors

Designer to choose only greyscale colors for use in the design.

Requirements
Must have
• Matte black as the background color. Clean lines and use of contrast. A specific design aspect that will use silver foil.
Nice to have
• Up in the air on integrating a QR code
Should not have
• Any houses or other real estate related design (ex: a clip art house)

```html
<!DOCTYPE html>
<html lang="en">
<head>
<meta charset="utf-8">
<title>Halvorsen Realty — Business Card</title>
<link href="https://fonts.googleapis.com/css2?family=Montserrat:wght@300;400;600&display=swap" rel="stylesheet">
<style>
  :root {
    --backdrop: #3b3b3d;
    --card-black: #141414;
    --foil-silver: #d9d9d9;
    --text-white: #f2f2f2;
    --text-grey: #8a8a8a;
    --rule-grey: #6e6e6e;
  }
  * { margin: 0; padding: 0; box-sizing: border-box; }
  html, body {
    width: 1200px; height: 801px; overflow: hidden;
    background: var(--backdrop);
    font-family: "Montserrat", sans-serif;
  }
  .sheet {
    width: 1200px; height: 801px;
    display: flex; align-items: center; justify-content: center; gap: 40px;
  }
  .card {
    width: 520px; height: 297px;
    background: var(--card-black);
    border-radius: 3px;
    position: relative;
    box-shadow: 0 10px 30px rgba(0,0,0,.35);
  }
  /* Brand lockup */
  .brand { display: flex; align-items: center; gap: 14px; color: var(--foil-silver); }
  .brand-circle {
    border: 2px solid var(--foil-silver); border-radius: 50%; flex: none;
  }
  .brand-name {
    font-weight: 300; text-transform: uppercase; line-height: 1.1;
    letter-spacing: .06em;
  }
  /* Agent side */
  .card-agent { display: flex; align-items: center; padding: 0 34px; }
  .card-agent .brand-circle { width: 50px; height: 50px; }
  .card-agent .brand-name { font-size: 22px; }
  .divider {
    width: 1px; height: 96px; background: var(--rule-grey);
    margin: 0 22px 0 24px; flex: none;
  }
  .agent-name {
    color: var(--text-white); font-weight: 600; font-size: 15px;
    letter-spacing: .03em; text-transform: uppercase;
  }
  .agent-title { color: var(--text-grey); font-size: 11px; font-weight: 300; margin: 2px 0 10px; }
  .contact-list { list-style: none; }
  .contact-list li {
    display: flex; align-items: center; gap: 7px;
    color: var(--text-white); font-size: 11px; font-weight: 300; margin-bottom: 4px;
  }
  .contact-list svg { width: 10px; height: 10px; fill: var(--text-grey); flex: none; }
  /* Logo side */
  .card-brand { display: flex; flex-direction: column; align-items: center; justify-content: center; }
  .card-brand .brand { gap: 18px; margin-top: 10px; }
  .card-brand .brand-circle { width: 78px; height: 78px; }
  .card-brand .brand-name { font-size: 34px; }
  .slogan {
    position: absolute; bottom: 42px; left: 0; right: 0; text-align: center;
    color: var(--text-grey); font-size: 11px; font-weight: 400;
    letter-spacing: .16em; text-transform: uppercase;
  }
</style>
</head>
<body>
<main class="sheet">
  <section class="card card-agent" aria-label="Agent side">
    <div class="brand">
      <span class="brand-circle"></span>
      <span class="brand-name">Halvorsen<br>Realty</span>
    </div>
    <span class="divider"></span>
    <div class="agent-info">
      <p class="agent-name">Daniel Hartley</p>
      <p class="agent-title">President</p>
      <ul class="contact-list">
        <li><svg viewBox="0 0 10 10"><path d="M2 0.5l2 2-1 1.2c.6 1.2 1.5 2.1 2.7 2.7L6.9 5.4l2 2-1.2 1.6C4.3 8.8 1.2 5.7 1 2.2z"/></svg>555-310-7842</li>
        <li><svg viewBox="0 0 10 10"><path d="M0 2h10v6H0z M0 2l5 3.5L10 2" fill="none" stroke="#8a8a8a" stroke-width="1"/></svg>dhartley@halvorsenrealty.com</li>
        <li><svg viewBox="0 0 10 10"><circle cx="5" cy="5" r="4.3" fill="none" stroke="#8a8a8a" stroke-width="1"/><path d="M0.7 5h8.6M5 0.7c-2 2.5-2 6.1 0 8.6M5 0.7c2 2.5 2 6.1 0 8.6" fill="none" stroke="#8a8a8a" stroke-width=".8"/></svg>www.halvorsenrealty.com</li>
      </ul>
    </div>
  </section>

  <section class="card card-brand" aria-label="Brand side">
    <div class="brand">
      <span class="brand-circle"></span>
      <span class="brand-name">Halvorsen<br>Realty</span>
    </div>
    <p class="slogan">Quietly Redefining Fine Homes</p>
  </section>
</main>
</body>
</html>
```